Brochure for Specialist Divorce Support

1. I want an A4 three fold brochure or DL to promote my business and services.
My market are people going through divorce and are usually feeling very overwhelmed and therefore not functioning very well - both men and women, age early forties,
2. Colours – variety of blues and lime greens but you choose if you need a contrast e.g. orange
3. Images – happy single families
4. Theme - could you make it around water please - soothing
5. Logos – HWN &; HWT (I will attach)
6. I have a lot of content so maybe not too busy but still professional feel +
warm and reassuring
7. I'm attaching -

- a draft brochure I put together using a Microsoft template
- a word document with extra details
- plus two logos to do with my qualifications
- and some images for you to choose from

7. I want to use this as a template for some other brochures -> more work for
the winner.

Target Market(s)

Men and women usually in their early forties with primary school aged children i.e 5 to 12 years old.
They are going through a divorce and very upset, Maybe losing contact with their children and their way of life as they know it is disappearing. They are in turmoil and not functioning as well as they usually do.

Industry/Entity Type

Business

Font styles to use
Sans Serif

Colors
34a7d7
abd037
3277b5

Requirements
Must have
• I want the brochure to be three folds with the center the full A4
• Could you make the theme around water please.
• I will upload some photos for you to use if you want,

```html
<!DOCTYPE html>
<html lang="en">
<head>
<meta charset="utf-8">
<title>Tailored Divorce Support</title>
<link href="https://fonts.googleapis.com/css2?family=Jost:wght@300;400;500;700;800&display=swap" rel="stylesheet">
<style>
:root{
  --stage:#dff5fc;
  --paper:#ffffff;
  --ink:#111111;
  --navy:#2b2f86;
  --teal:#1aa9c9;
  --sky:#34a7d7;
  --blue:#3277b5;
  --lime:#8dc63f;
  --lime-dark:#7ab648;
  --mark:#3277b5;
  --logo-blue:#2d4f9e;
  --logo-red:#d42b2b;
}
*{margin:0;padding:0;box-sizing:border-box}
html,body{width:1200px;height:1200px;overflow:hidden}
body{background:var(--stage);font-family:'Jost',sans-serif;color:var(--paper);position:relative}
.brochure{position:absolute;left:338px;top:42px;width:527px;height:1116px;background:var(--paper);overflow:hidden}
.header{position:absolute;left:0;top:0;width:527px;height:154px}
.header-photo{position:absolute;left:0;top:0;width:176px;height:154px;background:radial-gradient(ellipse at 45% 45%,#e8c5ae 0%,#c9977b 45%,#f4ece6 80%,#fff 100%)}
.owner{position:absolute;right:214px;top:56px;text-align:right;color:var(--ink);font-size:18px;line-height:22px;font-weight:400}
.divider{position:absolute;left:333px;top:30px;width:2px;height:100px;background:var(--navy)}
.title{position:absolute;left:356px;top:26px;color:var(--ink);font-size:32px;line-height:33px;font-weight:800;letter-spacing:.5px}
.water-scene{position:absolute;left:0;top:154px;width:527px;height:812px;background:linear-gradient(180deg,var(--teal) 0%,#6cc3dc 25%,#b9dde9 50%,#d9e6ef 75%,#e9eef4 100%)}

.frame{position:absolute;left:18px;width:499px;border:3px solid var(--paper);border-top:none}
.frame::before,.frame::after{content:"";position:absolute;top:0;height:3px;background:var(--paper)}
.frame::before{left:-3px;width:var(--gap-start)}
.frame::after{left:var(--gap-end);right:-3px}
.frame-fill{position:absolute;left:6px;right:6px;top:9px;bottom:6px;background:rgba(50,130,205,.85)}
.section-title{position:absolute;font-size:36px;font-weight:300;line-height:1;color:var(--paper);white-space:nowrap}

.services{top:202px;height:178px;--gap-start:34px;--gap-end:190px}
.services-title{left:67px;top:180px}
.cols{position:absolute;left:10px;top:22px;display:flex;gap:14px;font-size:10.6px;line-height:13px;font-weight:400}
.cols ul{list-style:none}
.cols ul:first-child{width:226px}
.cols ul:last-child{width:222px}
.cols li{position:relative;padding-left:10px;margin-bottom:17px}
.cols li::before{content:"";position:absolute;left:0;top:4px;width:5px;height:5px;border-radius:50%;background:var(--paper)}

.says{top:414px;height:212px;--gap-start:34px;--gap-end:286px}
.says-title{left:67px;top:392px}
.quotes{position:absolute;left:10px;top:28px;display:flex;gap:14px;font-size:11.2px;line-height:13px}
.quotes div:first-child{width:226px}
.quotes div:last-child{width:222px}
.quotes p{margin-bottom:16px;text-indent:-5px;padding-left:5px}

.testimonial{position:absolute;left:18px;top:664px;width:499px;height:282px;background:var(--lime);border-bottom-right-radius:60px}
.testimonial-title{left:73px;top:644px;z-index:2}
.client-photo{position:absolute;left:22px;top:51px;width:116px;height:166px;border:2px solid var(--paper);background:linear-gradient(180deg,#3a3a3a 0%,#8a8a8a 40%,#d9b8a4 60%,#2a2f4a 100%)}
.mark{position:absolute;font-size:110px;line-height:1;color:var(--mark);opacity:.7;font-weight:500}
.mark-open{left:176px;top:14px}
.mark-close{left:386px;top:168px}
.testimonial-text{position:absolute;left:156px;top:50px;width:324px;font-size:11.8px;line-height:14.5px}
.testimonial-text p{margin-bottom:14.5px}
.client-name{position:absolute;left:156px;top:240px;font-size:13px;font-weight:700}

.footer-details{position:absolute;left:0;top:966px;width:190px;height:150px;background:var(--lime)}
.footer-about{position:absolute;left:178px;top:966px;width:179px;height:150px;background:var(--lime-dark);border-top-right-radius:30px}
.footer-head{font-size:18px;font-weight:500;margin:6px 0 6px 18px}
.footer-body{font-size:10.5px;line-height:14.8px;margin-left:18px;font-weight:300}
.footer-about .footer-head,.footer-about .footer-body{margin-left:12px}
.accreditations{position:absolute;left:357px;top:966px;width:170px;height:150px;background:var(--paper)}
.cred{position:absolute;display:flex;align-items:center;gap:6px;font-weight:700;font-size:26px;color:var(--logo-blue)}
.cred-top{left:52px;top:34px}
.cred-bottom{left:48px;top:84px;color:var(--logo-red)}
.cred .dot{display:inline-block;width:14px;height:14px;border-radius:50%;background:currentColor}
</style>
</head>
<body>
<main class="brochure">
  <header class="header">
    <div class="header-photo" role="img" aria-label="Photo of a mother kissing her smiling baby"></div>
    <p class="owner">Helena<br>surname</p>
    <div class="divider"></div>
    <h1 class="title">Tailored<br>Divorce<br>Support</h1>
  </header>

  <div class="water-scene" role="img" aria-label="Soft background photo of a mother in a sun hat holding her baby against a blue sky"></div>

  <section class="frame services">
    <div class="frame-fill">
      <div class="cols">
        <ul>
          <li>Specialist divorce support to suit your needs;</li>
          <li>Pre-mediation coaching helping you prepare and achieve more positive outcomes to avoid going to court;</li>
          <li>Collaborative law coaching to increase crucial skills so you can participate more constructively in negotiations;</li>
        </ul>
        <ul>
          <li>Delivery of HWN Conflict Insight Profile giving you real feedback on the constructive and destructive behaviours you choose during conflict situations to facilitate more productive discussions;</li>
          <li>Corporate Conflict Management Training.</li>
        </ul>
      </div>
    </div>
  </section>
  <h2 class="section-title services-title">Services</h2>

  <section class="frame says">
    <div class="frame-fill">
      <div class="quotes">
        <div>
          <p>“Often family and friends can try to influence decisions based on what they see as best, so you can feel under an enormous pressure to keep them happy. Coaching offers an objective and neutral sounding board there just for you.”</p>
          <p>“Every divorce is different and families going forward will be different. I try to get my client to see or find ways they can co-parent as opposed to being one of two single parents.”</p>
        </div>
        <div>
          <p>“Even the most together person can be totally unprepared for the emotional overwhelm that divorce can bring, regardless if they are the one who made the decision to leave.”</p>
          <p>“Everyone is different and move through these stages at their own pace.”</p>
        </div>
      </div>
    </div>
  </section>
  <h2 class="section-title says-title">What they say</h2>

  <section class="testimonial">
    <div class="client-photo" role="img" aria-label="Portrait photo of the client giving the testimonial"></div>
    <span class="mark mark-open">“</span>
    <span class="mark mark-close">”</span>
    <div class="testimonial-text">
      <p>After many cups of coffee and long hours of listening to me, my very good friend suggested I speak to Maren, a divorce coach. I was a bit skeptical, especially when a phone session was suggested.</p>
      <p>From my first phone session I felt empowered. It gave me a sense of direction, assisted me to set realistic goals and action plans. Most importantly it aided my self esteem.</p>
      <p>Divorce is overwhelming. Talking to a caring professional like Helena helped me acknowledge my priorities and a way to achieve them. Thank you Helena.</p>
    </div>
    <p class="client-name">Dana - Cccccc, Smmmmm. AAA</p>
  </section>
  <h2 class="section-title testimonial-title">Testimonial</h2>

  <section class="footer-details">
    <h3 class="footer-head">DETAILS</h3>
    <p class="footer-body">Full details on my website<br>.......................................<br><br>or email:<br>helena@...</p>
  </section>
  <section class="footer-about">
    <h3 class="footer-head">ABOUT</h3>
    <p class="footer-body">Helena ............<br>HWT Certified Divorce Coach<br>Clearway Trained Conflict Coach<br>Cert IV in Training &amp; Assessment<br>Accredited in HWN Conflict<br>Insight Profile<br>BA (Ind. Relations) (UNV)</p>
  </section>
  <aside class="accreditations">
    <div class="cred cred-top"><span class="dot"></span>HWT</div>
    <div class="cred cred-bottom"><span class="dot"></span>HWN</div>
  </aside>
</main>
</body>
</html>
```